IT supplier clean wordpress website - payment guaranteed

Clean website design for a wordpress based website
Design only - PSD delivery with images

current website: www.quilmo.net
please use your imagination and try something out of the box...
We like https://trevanly.com.au as look and feel, but you don't have to copy it, you can be creative

We like the navigation header and the phone number, but do not need 'instant quote' so the 1300 phone number and the 'lock' icon for login can be on the same line

Site Map:
IT support
VoIP
Internet and Data
Cloud hosting
About
Contact

Our logo is attached, it can be used light or dark.
Our only color used is the warm grey Pantone 8003C hex #877A69

You will only need to design the homepage to win the competition, but the winning designer will be required to supply without extra charges:
1. Home page design
2. A second, standard page template design
3. An icon set in colors appropriate to the site that have icons to match the subjects in these pages:
https://trevanly.com.au/products/
https://trevanly.com.au/making-the-switch/
https://trevanly.com.au/why-trevanly/
We will create a single page version of the options on https://trevanly.com.au/solutions/
4.Any images used

Please avoid stock photos that are too common - e.g. smiling woman with headset, try to make the design stand out with simple images and well-designed layout.

Mid-size business clients

It Company

1 page

• Quil logo
• Use Quil color

```html
<!DOCTYPE html>
<html lang="en">
<head>
<meta charset="utf-8">
<title>Quil – IT outsourcing</title>
<link href="https://fonts.googleapis.com/css2?family=Open+Sans:wght@400;600;700&display=swap" rel="stylesheet">
<style>
:root{
  --brand:#877A69;
  --brand-dark:#716555;
  --ink:#333333;
  --muted:#777777;
  --card:#efefef;
  --panel:#333333;
  --footer:#2a2a2a;
  --accent:#e7b73a;
  --white:#ffffff;
}
*{box-sizing:border-box;margin:0;padding:0}
html,body{width:675px;height:1200px;overflow:hidden}
body{font-family:"Open Sans",Arial,sans-serif;color:var(--ink);background:var(--white);position:relative}
.hero{position:absolute;left:0;top:0;width:675px;height:370px;
  background:linear-gradient(100deg,#5d5a57 0%,#8d8a86 35%,#b9b6b1 60%,#9c9893 80%,#7a7672 100%)}
.topbar{position:absolute;right:0;top:0;height:22px;width:215px;background:var(--brand);color:var(--white);
  font-size:9px;display:flex;align-items:center;justify-content:flex-end;gap:14px;padding-right:14px}
.topbar span{display:flex;align-items:center;gap:4px}
.navbar{position:absolute;left:0;top:28px;width:675px;height:32px;background:rgba(255,255,255,.92)}
.nav{position:absolute;right:18px;top:0;display:flex;height:32px;list-style:none}
.nav li{font-size:10.5px;padding:0 11px;display:flex;align-items:center;color:var(--ink)}
.nav li.active{background:var(--brand);color:var(--white)}
.logo{position:absolute;left:27px;top:0;width:84px;height:96px;background:var(--white);
  border:2px solid var(--brand);border-top:none;border-radius:0 0 10px 10px;display:flex;align-items:flex-end;justify-content:center;padding-bottom:22px}
.logo span{font-size:22px;font-weight:600;color:var(--brand)}
.intro{position:absolute;top:388px;width:675px;text-align:center;font-size:20px;font-weight:600;color:#2d2d2d}
.card{position:absolute;top:462px;width:176px;height:180px;background:var(--card);text-align:center;padding:18px 14px 0}
.card h3{font-size:12.5px;font-weight:600;color:#2d2d2d;letter-spacing:.3px}
.card .divider{margin:6px auto 8px;display:block}
.card p{font-size:8.2px;line-height:1.5;color:var(--muted)}
.card .btn{display:inline-block;margin-top:10px;font-size:7.5px;padding:3px 9px;background:var(--white);color:var(--muted);border:1px solid #d5d5d5}
.card.featured{top:446px;height:198px;background:var(--brand);padding-top:22px}
.card.featured h3,.card.featured p{color:var(--white)}
.card.featured .btn{background:var(--accent);color:#3a3020;border-color:var(--accent)}
.help{position:absolute;top:676px;left:0;width:675px;height:244px;
  background:linear-gradient(180deg,#8a7d6c,var(--brand) 50%,#7d7161)}
.help h2{position:absolute;left:30px;top:14px;font-size:15px;font-weight:400;color:var(--white)}
.help h2 b{font-weight:600}
.help .lead{position:absolute;left:30px;top:40px;width:385px;font-size:7.5px;line-height:1.5;color:#f1ece5}
.field{position:absolute;left:30px;width:120px;height:18px;background:var(--white);font-size:7px;color:#999;padding:4px 6px}
.message{position:absolute;left:160px;top:90px;width:250px;height:116px;background:var(--white);font-size:7px;color:#999;padding:5px 6px}
.send{position:absolute;left:30px;top:216px;width:52px;height:20px;background:var(--accent);font-size:8px;font-weight:600;color:#3a3020;display:flex;align-items:center;justify-content:center}
.contact{position:absolute;left:460px;top:18px;width:182px;height:198px;background:var(--panel);color:var(--white);padding:14px 14px}
.contact h3{font-size:12.5px;font-weight:400;letter-spacing:.5px;margin-bottom:14px}
.contact li{list-style:none;display:flex;gap:8px;font-size:7.5px;line-height:1.4;margin-bottom:10px;align-items:flex-start}
.contact svg{flex:none}
.partners{position:absolute;top:946px;width:675px;text-align:center;font-size:17px;font-weight:600;color:#2d2d2d}
.badge{position:absolute;top:1002px;width:72px;height:56px;border:1px solid #dcdcdc;background:#f6f6f6}
.badge.dark{background:#1f4f6b;border-color:#1f4f6b}
.footer{position:absolute;top:1096px;left:0;width:675px;height:104px;background:var(--footer);color:#cfcfcf;text-align:center}
.footer ul{list-style:none;display:flex;justify-content:center;gap:8px;padding-top:18px;font-size:8.5px;color:var(--white)}
.footer .sep{color:#888}
.footer .copy{font-size:7.5px;margin-top:6px}
.social{display:flex;justify-content:center;gap:7px;margin-top:10px}
.social span{width:16px;height:16px;border-radius:50%;background:#555}
</style>
</head>
<body>
<div class="hero" role="img" aria-label="Businesswoman in a grey suit holding a briefcase in front of a chalk wall sketched with network diagrams"></div>

<div class="topbar">
  <span><svg width="8" height="8" viewBox="0 0 10 10"><path d="M2 1l2 0 1 2.5-1.3 1a5 5 0 0 0 2.8 2.8l1-1.3L10 7v2c0 .5-.5 1-1 1A9 9 0 0 1 0 2c0-.5.5-1 1-1z" fill="#fff"/></svg>Call us : 1300 555 019</span>
  <span><svg width="7" height="9" viewBox="0 0 7 9"><rect x="0" y="4" width="7" height="5" fill="#fff"/><path d="M1.5 4V2.5a2 2 0 0 1 4 0V4" stroke="#fff" fill="none"/></svg>LOGIN</span>
</div>
<div class="navbar">
  <ul class="nav">
    <li class="active">IT support</li><li>VoIP</li><li>Internet and Data</li><li>Cloud hosting</li><li>About</li><li>Contact</li>
  </ul>
</div>
<div class="logo"><span>Quil</span></div>

<h1 class="intro">IT outsourcing the way it should be</h1>

<div class="card" style="left:62px">
  <h3>DATA AND VOICE</h3>
  <svg class="divider" width="60" height="8"><line x1="0" y1="4" x2="24" y2="4" stroke="#ccc"/><circle cx="30" cy="4" r="3" fill="var(--accent)"/><line x1="36" y1="4" x2="60" y2="4" stroke="#ccc"/></svg>
  <p>Quil supplies a wide range of business data connections which are reliable, scalable, fast and represent excellent value for money. Choose from a wide range of delivery methods and plans.</p>
  <span class="btn">Learn More</span>
</div>
<div class="card featured" style="left:250px">
  <h3>CLOUD SERVICES</h3>
  <svg class="divider" width="60" height="8"><line x1="0" y1="4" x2="24" y2="4" stroke="#bfb3a3"/><circle cx="30" cy="4" r="3" fill="var(--accent)"/><line x1="36" y1="4" x2="60" y2="4" stroke="#bfb3a3"/></svg>
  <p>Quil supplies a wide range of business data connections which are reliable, scalable, fast and represent excellent value for money. Choose from a wide range of delivery methods and plans. From simple Internet</p>
  <span class="btn">Learn More</span>
</div>
<div class="card" style="left:438px">
  <h3>SUPPORT</h3>
  <svg class="divider" width="60" height="8"><line x1="0" y1="4" x2="24" y2="4" stroke="#ccc"/><circle cx="30" cy="4" r="3" fill="var(--accent)"/><line x1="36" y1="4" x2="60" y2="4" stroke="#ccc"/></svg>
  <p>A wide range of skills and certifications with a great bedside manner. Casual Service Service done on an on call basis. Only pay for what you need, when you need it. The same level of professional</p>
  <span class="btn">Learn More</span>
</div>

<section class="help">
  <h2>You have questions?<b>AND NEED MORE HELP?</b></h2>
  <p class="lead">Need more details about our plans? That is easy. Keep running your business and let our team handle the technology for you. Talk today with one of our friendly advisors.</p>
  <div class="field" style="top:92px">Your name</div>
  <div class="field" style="top:122px">Your email</div>
  <div class="field" style="top:152px">Your phone</div>
  <div class="field" style="top:182px">Your subject</div>
  <div class="message">How can we help ?</div>
  <div class="send">SEND</div>
  <div class="contact">
    <h3>CONTACT DETAILS</h3>
    <ul>
      <li><svg width="10" height="10" viewBox="0 0 10 10"><circle cx="5" cy="5" r="5" fill="#fff"/><path d="M5 2a2 2 0 0 0-2 2c0 1.5 2 4 2 4s2-2.5 2-4a2 2 0 0 0-2-2z" fill="#333"/></svg><span>Street Address<br>Suite 4, 22 Harlow Lane,<br>Kestrel NSW 2099</span></li>
      <li><svg width="10" height="10" viewBox="0 0 10 10"><circle cx="5" cy="5" r="5" fill="#fff"/><circle cx="5" cy="5" r="2.5" fill="none" stroke="#333"/></svg><span>http://quilmo.net.au</span></li>
      <li><svg width="10" height="10" viewBox="0 0 10 10"><circle cx="5" cy="5" r="5" fill="#fff"/><rect x="3.5" y="2.5" width="3" height="5" rx=".6" fill="#333"/></svg><span>P +61 (2) 5550 1122</span></li>
      <li><svg width="10" height="10" viewBox="0 0 10 10"><circle cx="5" cy="5" r="5" fill="#fff"/><rect x="2.5" y="3" width="5" height="4" fill="#333"/></svg><span>F +61 (2) 5550 1133</span></li>
      <li><svg width="10" height="10" viewBox="0 0 10 10"><circle cx="5" cy="5" r="5" fill="#fff"/><rect x="2.5" y="3.2" width="5" height="3.6" fill="none" stroke="#333" stroke-width=".8"/><path d="M2.5 3.2 5 5.3 7.5 3.2" fill="none" stroke="#333" stroke-width=".8"/></svg><span>info@quilmo.net</span></li>
    </ul>
  </div>
</section>

<h2 class="partners">Our Partners</h2>
<div class="badge" style="left:188px"></div>
<div class="badge" style="left:302px"></div>
<div class="badge dark" style="left:416px"></div>

<footer class="footer">
  <ul><li>IT support</li><li class="sep">|</li><li>VoIP</li><li class="sep">|</li><li>Internet and Data</li><li class="sep">|</li><li>Cloud hosting</li><li class="sep">|</li><li>About</li><li class="sep">|</li><li>Contact</li></ul>
  <p class="copy">Copyright 2017 © www.quilmo.net. All Rights Reserved</p>
  <div class="social"><span></span><span></span><span></span><span></span></div>
</footer>
</body>
</html>
```